International Life Insurer Needs a Web Design

What We Do: We are a boutique financial services firm specializing in solutions that financial services professionals can integrate into comprehensive wealth preservation strategies for their clients. Strategies we provide may run the spectrum from simple life insurance products to complex cases with very sophisticated and intricate solutions.

Industry Type: Financial & Insurance

Top Things to Communicate Through Our Web Design:
#1 Ultra High Net Worth
#2 INTERNATIONAL
#3 Private Banking
#4 Expertise
________________________________________
Our Target Audience:
Financial institutions/private banks who have high net worth/ultra high net worth international clients looking for unparalleled expertise in wealth preservation, taxation, and business insurance. The audience is the financial service professional, not the end client of the financial services. We will direct the professional to the site.
We Like These Designs. (fonts, colors, style):
Simple font, clean, modern, contemporary, blue colors
NOT stodgy, old, gothic, etc.

Secondarily, we’d like to also create a small tri-fold brochure incorporating the web elements (design, text), so the ability to transfer the design to print might be a plus.
Updates

Target Market(s)

Financial services professionals catering to their ultra high net worth clients

Industry/Entity Type

Life Insurance

Requirements
Must have
• Our logo (see uploaded file)
Nice to have
• the existing website includes some text that could be reviewed for ideas and incorporated into the design: http://harborlinecoveragepartners.example/

```html
<!DOCTYPE html>
<html lang="en">
<head>
<meta charset="utf-8">
<title>Harborline Coverage Partners</title>
<link rel="stylesheet" href="https://fonts.googleapis.com/css2?family=Carlito:ital,wght@0,400;0,700;1,400&family=Open+Sans:wght@300&family=Roboto+Condensed:wght@300&display=swap">
<style>
  :root {
    --navy: #123c78;
    --navy-dark: #0b326b;
    --navy-light: #2a5c9c;
    --brand-text: #1d3f8a;
    --accent: #0a86cf;
    --ink: #222;
    --muted: #666;
    --page: #ebebeb;
    --stripe: #e3e3e3;
    --card: #ffffff;
    --rule: #d6d6d6;
  }
  * { box-sizing: border-box; margin: 0; padding: 0; }
  html, body { width: 1200px; height: 1000px; overflow: hidden; }
  body {
    position: relative;
    font-family: "Carlito", "Calibri", sans-serif;
    color: var(--ink);
    background: repeating-linear-gradient(90deg, var(--page) 0 3px, var(--stripe) 3px 4px);
  }
  .masthead {
    position: absolute; left: 0; top: 0; width: 1200px; height: 410px;
    background: linear-gradient(180deg, #ffffff 0%, #f4f8fb 60%, #dfeef8 100%);
    border-bottom: 1px solid var(--rule);
  }
  .masthead::after {
    content: ""; position: absolute; left: 0; right: 0; top: 40px; height: 130px;
    background: linear-gradient(180deg, rgba(190,225,245,0) 0%, rgba(175,218,242,.55) 80%, rgba(190,225,245,0) 100%);
    pointer-events: none;
  }
  .brand {
    position: absolute; left: 140px; top: 30px; display: flex; align-items: center; gap: 6px;
    z-index: 2;
  }
  .brand-mark { width: 55px; height: 55px; background: var(--navy-light); }
  .brand-name {
    font-family: "Carlito", sans-serif; font-weight: 400; font-size: 25px; line-height: 21px;
    color: var(--brand-text); letter-spacing: -0.5px;
  }
  .search {
    position: absolute; left: 899px; top: 30px; width: 180px; height: 24px;
    background: #fff; border: 1px solid #b9b9b9; z-index: 2;
  }
  .search svg { position: absolute; right: 2px; top: 3px; }
  .main-nav {
    position: absolute; left: 120px; top: 120px; width: 960px; height: 30px;
    background: linear-gradient(180deg, var(--navy-light) 0 50%, var(--navy-dark) 50% 100%);
    z-index: 2;
  }
  .main-nav ul { list-style: none; display: flex; justify-content: flex-end; height: 30px; padding-right: 30px; }
  .main-nav li {
    color: #fff; font-size: 12px; line-height: 30px; text-transform: uppercase;
    margin-left: 33px; position: relative; padding-left: 11px;
  }
  .main-nav li::before {
    content: ""; position: absolute; left: 0; top: 12px; width: 4px; height: 4px;
    border-right: 1.5px solid #fff; border-bottom: 1.5px solid #fff; transform: rotate(-45deg);
  }
  .main-nav li.current::before { transform: rotate(45deg); top: 10px; }
  .hero {
    position: absolute; left: 120px; top: 150px; width: 960px; height: 240px;
    background: #fff; border: 1px solid var(--rule); border-top: 0; z-index: 2;
  }
  .hero-title {
    position: absolute; left: 18px; top: 34px;
    font-family: "Open Sans", sans-serif; font-weight: 300; font-size: 32px; color: var(--navy);
  }
  .hero-lead {
    position: absolute; left: 20px; top: 78px; width: 370px;
    font-size: 15.5px; line-height: 17px; color: #333;
  }
  .hero-photo {
    position: absolute; right: 0; top: 0; width: 503px; height: 239px;
    background: linear-gradient(120deg, #f4f6f8 0%, #c7d8ec 35%, #e9dfd6 60%, #f2f2f3 80%, #d8d8dc 100%);
  }
  .panel {
    position: absolute; top: 430px; width: 300px; height: 220px; background: var(--card);
    border-top: 4px solid var(--accent); box-shadow: 0 1px 4px rgba(0,0,0,.35);
    padding: 18px 20px 0;
  }
  .panel.what { left: 130px; }
  .panel.why { left: 450px; }
  .panel.contact { left: 780px; }
  .panel h2 {
    font-family: "Roboto Condensed", sans-serif; font-weight: 300; font-size: 24px;
    color: var(--navy); margin-bottom: 11px; letter-spacing: -0.3px;
  }
  .panel p { font-size: 12px; line-height: 14.5px; text-indent: 36px; margin-bottom: 7px; }
  .panel ul { list-style: none; margin-top: 3px; }
  .panel li { font-size: 12px; line-height: 14px; padding-left: 16px; position: relative; margin-bottom: 7.5px; }
  .panel li::before {
    content: ""; position: absolute; left: 0; top: 4px; width: 6px; height: 6px; background: #333;
  }
  .contact-list { list-style: none; margin-top: 12px; }
  .panel .contact-list li { display: flex; align-items: center; padding-left: 0; height: 22px; margin-bottom: 8px; }
  .panel .contact-list li::before { display: none; }
  .contact-list .icon { width: 22px; height: 22px; border-radius: 2px; background: linear-gradient(180deg,#2f8fd6,#0c5aa6); margin-right: 19px; flex: none; display: flex; align-items: center; justify-content: center; }
  .contact-list .phone { font-style: italic; }
  .site-footer {
    position: absolute; left: 120px; top: 700px; width: 960px; height: 100px;
    background: #fff; border-top: 4px solid var(--accent);
    text-align: right; padding: 28px 10px 0 0; color: var(--muted); font-size: 12px;
  }
  .site-footer p { margin-bottom: 7px; }
  .site-footer .sep { margin: 0 6px; }
</style>
</head>
<body>
  <header class="masthead">
    <div class="brand">
      <div class="brand-mark"></div>
      <div class="brand-name">Harborline Coverage<br>Partners</div>
    </div>
    <div class="search">
      <svg width="16" height="16" viewBox="0 0 16 16"><circle cx="6.5" cy="6.5" r="4.5" fill="none" stroke="#999" stroke-width="1.6"/><line x1="10" y1="10" x2="14.5" y2="14.5" stroke="#999" stroke-width="2"/></svg>
    </div>
    <nav class="main-nav">
      <ul>
        <li class="current">Home</li>
        <li>About Us</li>
        <li>Solutions for Diverse Needs</li>
        <li>Case Studies</li>
        <li>Contact</li>
      </ul>
    </nav>
    <section class="hero">
      <h1 class="hero-title">Strategic financial solutions</h1>
      <p class="hero-lead">Lorem ipsum dolor sit amet, consectetur adipiscing elit. Praesent ut lectus et eros vestibulum volutpat euismod eu erat. Curabitur vitae velit nulla, id porta elit.</p>
      <div class="hero-photo" role="img" aria-label="Photo of advisors' hands with pens reviewing printed financial charts"></div>
    </section>
  </header>

  <section class="panel what">
    <h2>What We Do</h2>
    <p>At Harborline Coverage Partners, protecting your clients’ families, their businesses, and their lifestyles are at the forefront of all we do.</p>
    <ul>
      <li>Unsurpassed service, support, and underwriting</li>
      <li>Licensed to conduct business nationally</li>
      <li>Advising businesses and families for over 50 years</li>
      <li>Independent, objective, and resourceful</li>
    </ul>
  </section>

  <section class="panel why">
    <h2>Why Us</h2>
    <p>There are many advantages to working with Harborline Coverage Partners. We offer the service and attention of a boutique agency, while leveraging the strength of preeminent American and offshore life insurance companies.</p>
    <p>In addition, since we are privately owned we base our actions and recommendations on what is best for our clients without regard to stockholder profit or share price.</p>
  </section>

  <section class="panel contact">
    <h2>Get In Touch</h2>
    <p>There are many advantages to working with Harborline Coverage Partners.</p>
    <ul class="contact-list">
      <li><span class="icon"><svg width="14" height="14" viewBox="0 0 14 14"><path d="M3 1l2.5 3-1.3 1.3c.8 1.8 2 3 3.6 3.7L9.1 7.7 12 10.2 10.6 12.8C6 12.5 1.5 8 1.2 3.4z" fill="#fff"/></svg></span><span class="phone">05550192846</span></li>
      <li><span class="icon"><svg width="14" height="10" viewBox="0 0 14 10"><rect x=".5" y=".5" width="13" height="9" fill="#fff"/><path d="M.5 .5L7 6l6.5-5.5" fill="none" stroke="#0c5aa6" stroke-width="1.2"/></svg></span>info@harborlinecoveragepartners.example</li>
      <li><span class="icon"></span>Follow Us on Chatterline</li>
    </ul>
  </section>

  <footer class="site-footer">
    <p>Copyright © 2012 Harborline Coverage Partners. All rights reserved.</p>
    <p>Disclaimer<span class="sep">|</span>Sitemap<span class="sep">|</span> Privacy Policy</p>
  </footer>
</body>
</html>
```